Banner Ad Design Project

hi i need several banner for a casino website
for examples you can visit some of the online casinos on the net.

the banners i need:

1. sportsbook
2. live casino
3. blackjack
4. slot games
5. bonus (e.g. Christmass bonus "double your deposit!" or "free spins"
6. "Do you want to win a trip to Las Vegas? Join now!"

if possible with some movement (flash/html5)

i have updated the prices!

payment committed! 

Reason: Error by brieflane End day was similar on start day

Industry/Entity Type

Casino

```html
<!DOCTYPE html>
<html lang="en">
<head>
<meta charset="utf-8">
<title>Live Casino Banner</title>
<link rel="stylesheet" href="https://fonts.googleapis.com/css2?family=Open+Sans:wght@700;800&display=swap">
<style>
  :root {
    --ink-black: #070707;
    --ink-deep: #141414;
    --table-grey: #6d6d6d;
    --table-light: #a9a9a9;
    --table-red: #b3121a;
    --button-red: #c4141b;
    --button-dark: #8a0b10;
    --text-white: #ffffff;
    --portrait-dark: #2a1d18;
    --portrait-skin: #c79a82;
  }
  * { margin: 0; padding: 0; box-sizing: border-box; }
  html, body {
    width: 1200px;
    height: 148px;
    overflow: hidden;
    background: var(--ink-black);
  }
  .banner {
    position: relative;
    width: 1200px;
    height: 148px;
    overflow: hidden;
    background: linear-gradient(90deg, var(--ink-black) 0%, var(--ink-deep) 28%, #1a1a1a 34%);
    font-family: "Open Sans", Arial, sans-serif;
  }
  .table-scene {
    position: absolute;
    left: 330px;
    top: 0;
    width: 760px;
    height: 148px;
    background:
      linear-gradient(90deg, var(--ink-deep) 0%, rgba(20,20,20,0) 14%),
      linear-gradient(180deg, rgba(0,0,0,0.35) 0%, rgba(0,0,0,0) 30%, rgba(0,0,0,0) 70%, rgba(0,0,0,0.4) 100%),
      linear-gradient(90deg, var(--table-grey) 0%, #5e5e5e 40%, var(--table-light) 75%, #8f8f8f 100%);
  }
  .table-accent {
    position: absolute;
    left: 900px;
    top: 0;
    width: 180px;
    height: 148px;
  }
  .portrait {
    position: absolute;
    right: 0;
    top: 0;
    width: 185px;
    height: 148px;
    background:
      radial-gradient(ellipse 55% 45% at 55% 35%, var(--portrait-skin) 0%, rgba(199,154,130,0) 100%),
      linear-gradient(180deg, var(--portrait-dark) 0%, #4a3328 60%, #1c1310 100%);
  }
  .play-button {
    position: absolute;
    left: 66px;
    top: 45px;
    width: 232px;
    height: 58px;
    border-radius: 12px;
    background: linear-gradient(180deg, #e3262d 0%, var(--button-red) 50%, var(--button-dark) 100%);
    box-shadow: inset 0 1px 0 rgba(255,255,255,0.35), 0 2px 4px rgba(0,0,0,0.6);
    color: var(--text-white);
    font-weight: 700;
    font-size: 27px;
    letter-spacing: 0.5px;
    display: flex;
    align-items: center;
    justify-content: center;
    text-decoration: none;
  }
  .headline {
    position: absolute;
    left: 438px;
    top: 42px;
    color: var(--text-white);
    font-weight: 800;
    font-size: 56px;
    line-height: 1;
    letter-spacing: -0.5px;
    text-shadow: 0 2px 4px rgba(0,0,0,0.85), 0 0 2px #000;
    white-space: nowrap;
  }
</style>
</head>
<body>
  <div class="banner">
    <div class="table-scene" role="img" aria-label="Blurred roulette table layout with numbered red and black squares"></div>
    <svg class="table-accent" viewBox="0 0 180 148" aria-hidden="true">
      <polyline points="20,0 90,70 20,148" fill="none" stroke="var(--table-red)" stroke-width="6"/>
      <polyline points="70,0 140,70 70,148" fill="none" stroke="var(--table-red)" stroke-width="6"/>
    </svg>
    <div class="portrait" role="img" aria-label="Dealer holding two playing cards"></div>
    <a class="play-button" href="#">PLAY NOW</a>
    <h1 class="headline">LIVE CASINO</h1>
  </div>
</body>
</html>
```